VELINTA Promotions - Business Card Design Project

We are looking for a classy business cards for Promotion Company based in Toronto, Canada named Velinta Promotions.

Velinta Promotions has an idea and vision to set high standard, be EXCLUSIVE and attract a group of people that will follow us through events we promote (night clubs, brand promotions, music events, and sport events)

We want to present a high standards and classy image to the others...
Updates

Target Market(s)

male/female age 25-40 Target: business owners young entrepreneur - clubing industry - media industry - promotion industry - marketing media industry

Industry/Entity Type

Events

Requirements
Must have
• business cards should be classy, make people feel exclusive , make people react ..

```html
<!DOCTYPE html>
<html lang="en">
<head>
<meta charset="utf-8">
<title>Velinta Promotions – Business Cards</title>
<link href="https://fonts.googleapis.com/css2?family=Cinzel:wght@400;600&display=swap" rel="stylesheet">
<style>
  :root {
    --stage: #000000;
    --card-dark: #05051a;
    --card-border: #e6e6e6;
    --ornament-blue: #3b33c4;
    --ornament-blue-deep: #2a25a0;
    --rule-blue: #2f55d8;
    --logo-cyan: #7fd3e8;
    --card-sky: #29a9e1;
    --logo-pale: #9fdcf2;
    --damask-white: #ffffff;
    --damask-grey: #d6d6d6;
  }
  html, body {
    margin: 0;
    padding: 0;
    overflow: hidden;
    background: var(--stage);
  }
  .canvas {
    position: relative;
    width: 1200px;
    height: 1149px;
    background: var(--stage);
    overflow: hidden;
  }

  /* Front card (dark) */
  .card-front {
    position: absolute;
    left: 301px;
    top: 107px;
    width: 799px;
    height: 455px;
    background: var(--card-dark);
    border: 2px solid var(--card-border);
    box-sizing: border-box;
    overflow: hidden;
  }
  .card-front .ornament-band {
    position: absolute;
    left: 0;
    top: 0;
    width: 100%;
    height: 238px;
    background: linear-gradient(180deg, var(--ornament-blue) 0%, var(--ornament-blue-deep) 70%, var(--card-dark) 100%);
  }
  .card-front .rule {
    position: absolute;
    left: 0;
    top: 397px;
    width: 100%;
    height: 3px;
    background: var(--rule-blue);
  }
  .card-front .ornament-strip {
    position: absolute;
    left: 0;
    top: 404px;
    width: 100%;
    height: 47px;
    background: linear-gradient(180deg, var(--ornament-blue-deep), var(--ornament-blue));
  }

  /* Name block */
  .brand {
    position: absolute;
    display: flex;
    flex-direction: column;
    align-items: center;
    font-family: "Cinzel", serif;
    font-weight: 400;
    line-height: 1;
  }
  .brand .name {
    font-size: 70px;
    letter-spacing: 4px;
  }
  .brand .tagline {
    font-size: 20px;
    letter-spacing: 9px;
    margin-top: 6px;
    align-self: flex-end;
  }
  .card-front .brand {
    left: 110px;
    top: 255px;
    width: 590px;
    color: var(--logo-cyan);
  }

  /* Back card (sky blue) */
  .card-back {
    position: absolute;
    left: 153px;
    top: 623px;
    width: 753px;
    height: 434px;
    overflow: hidden;
  }
  .card-back .damask-panel {
    position: absolute;
    left: 0;
    top: 0;
    width: 289px;
    height: 100%;
    background: linear-gradient(135deg, var(--damask-white) 0%, var(--damask-grey) 50%, var(--damask-white) 100%);
  }
  .card-back .color-panel {
    position: absolute;
    left: 289px;
    top: 0;
    right: 0;
    height: 100%;
    background: var(--card-sky);
  }
  .card-back .brand {
    left: 310px;
    top: 183px;
    width: 430px;
    color: var(--logo-pale);
  }
  .card-back .brand .name {
    font-size: 50px;
    letter-spacing: 3px;
  }
  .card-back .brand .tagline {
    font-size: 14px;
    letter-spacing: 6px;
    margin-top: 4px;
  }
</style>
</head>
<body>
<div class="canvas">
  <section class="card-front">
    <div class="ornament-band" role="img" aria-label="Blue ornamental damask pattern band"></div>
    <div class="brand">
      <span class="name">VELINTA</span>
      <span class="tagline">PROMOTIONS</span>
    </div>
    <div class="rule"></div>
    <div class="ornament-strip" role="img" aria-label="Blue ornamental damask border strip"></div>
  </section>

  <section class="card-back">
    <div class="damask-panel" role="img" aria-label="Light grey damask pattern panel"></div>
    <div class="color-panel"></div>
    <div class="brand">
      <span class="name">VELINTA</span>
      <span class="tagline">PROMOTIONS</span>
    </div>
  </section>
</div>
</body>
</html>
```